M25 Billboard Advert Required Please

I need an advert for a motorway Billboard on the M25 , the advert should show the following in big letters:
GUTTER CLEANING
DALRYNFLUES.COM and a small logo off to the side (Our logo is attached)

The printer has requested the following (Important please) the advert has to be
pdf file / 300 dpi/landscape orientation / scaled to a minimum 25% advert size ( this particular site is 22ft x 10ft so 25% of this please). Please also make sure that the artwork is embedded and outlined correctly if this is incorrect it will affect the printing of the banner.

Target Market(s)

General Public

Industry/Entity Type

Gutter Cleaning

Requirements
Should not have
• No Change to our Logo

```html
<!DOCTYPE html>
<html lang="en">
<head>
<meta charset="UTF-8">
<title>Gutter Cleaning Billboard</title>
<link href="https://fonts.googleapis.com/css2?family=League+Spartan:wght@600;700&family=Open+Sans:wght@700&display=swap" rel="stylesheet">
<style>
  :root {
    --backdrop: #a7a9a8;
    --paper: #ffffff;
    --ink: #0d0d0d;
    --accent-red: #c1272d;
    --photo-dark: #4d524e;
    --photo-mid: #6e6259;
    --photo-warm: #8a6a47;
    --photo-slate: #5e5f63;
  }
  html, body {
    margin: 0;
    padding: 0;
    width: 1200px;
    height: 722px;
    overflow: hidden;
    background: var(--backdrop);
  }
  .billboard {
    position: absolute;
    left: 107px;
    top: 131px;
    width: 982px;
    height: 446px;
    background: var(--paper);
    overflow: hidden;
  }
  .billboard__photo {
    position: absolute;
    inset: 0;
    width: 982px;
    height: 446px;
  }
  .brand {
    position: absolute;
    left: 37px;
    top: 38px;
  }
  .brand__row {
    display: flex;
    align-items: center;
    gap: 10px;
  }
  .brand__mark {
    width: 14px;
    height: 14px;
    background: var(--accent-red);
  }
  .brand__name {
    font-family: "League Spartan", sans-serif;
    font-weight: 700;
    font-size: 34px;
    line-height: 1;
    color: var(--ink);
    letter-spacing: -0.5px;
  }
  .brand__tagline {
    margin-top: 10px;
    font-family: "Open Sans", sans-serif;
    font-weight: 700;
    font-size: 12.5px;
    color: #222;
    letter-spacing: 0.1px;
  }
  .headline {
    position: absolute;
    left: 26px;
    top: 146px;
    margin: 0;
    font-family: "League Spartan", sans-serif;
    font-weight: 700;
    font-size: 86px;
    line-height: 96px;
    letter-spacing: -0.5px;
  }
  .headline__line { display: block; }
  .headline__line--dark { color: var(--ink); }
  .headline__line--red { color: var(--accent-red); }
  .web-address {
    position: absolute;
    left: 39px;
    top: 374px;
    margin: 0;
    font-family: "League Spartan", sans-serif;
    font-weight: 700;
    font-size: 45px;
    line-height: 1;
    color: var(--ink);
    letter-spacing: 0;
  }
</style>
</head>
<body>
  <div class="billboard">
    <svg class="billboard__photo" viewBox="0 0 982 446" role="img" aria-label="Close-up photo of a grey metal gutter with a perforated guard, filled with dry brown leaves, beside dark asphalt roof shingles">
      <defs>
        <linearGradient id="photoTone" x1="0" y1="0" x2="1" y2="0.4">
          <stop offset="0" stop-color="var(--photo-dark)"/>
          <stop offset="0.35" stop-color="var(--photo-mid)"/>
          <stop offset="0.6" stop-color="var(--photo-warm)"/>
          <stop offset="1" stop-color="var(--photo-slate)"/>
        </linearGradient>
      </defs>
      <polygon points="231,0 982,0 982,446 686,446" fill="url(#photoTone)"/>
    </svg>

    <div class="brand">
      <div class="brand__row">
        <span class="brand__mark"></span>
        <span class="brand__name">Dalryn Flues</span>
      </div>
      <div class="brand__tagline">Clean gutters protect your property</div>
    </div>

    <h1 class="headline">
      <span class="headline__line headline__line--dark">GUTTER</span>
      <span class="headline__line headline__line--red">CLEANING</span>
    </h1>

    <p class="web-address">DALRYNFLUES.COM</p>
  </div>
</body>
</html>
```